Luxury Bath Flyer

I would like to have a professional Flyer, which would describe a beautiful atmospheric luxury-Bath situation. I am sending you a( screenshot) Flyer Proposal, which shoes my intention and wish how I would like to have it. Please note that Ästhetik and a professional Flyer is very important to me. If possible send a psd.file or a indesign file, in case of we gonna need to change the text. You are also free to make 2 different proposals and one as you would suggest.?(I send you couple pictures, but the main one which I choose on the pdf file, please keep that, it is called " BE-03" - If there is a question please let me know. Looking forward to receive an amazing artwork.Kind Regards Dilek

```html
<!DOCTYPE html>
<html lang="de">
<head>
<meta charset="utf-8">
<title>Badwerk – Ihr exklusives Bad zum Fixpreis</title>
<link rel="stylesheet" href="https://fonts.googleapis.com/css2?family=Montserrat:ital,wght@0,400;0,500;0,600;0,700;1,700;1,800&display=swap">
<style>
  :root {
    --navy: #1e3850;
    --blue: #26a3dc;
    --orange: #f5a11e;
    --panel: #333538;
    --ink: #1e3850;
    --stage: #ededed;
    --paper: #f7f7f6;
    --photo-light: #ece8e3;
    --photo-mid: #d9cfc4;
    --photo-warm: #c98f67;
  }
  html, body {
    margin: 0;
    width: 1200px;
    height: 1200px;
    overflow: hidden;
    background: var(--stage);
  }
  .flyer {
    position: absolute;
    left: 200px;
    top: 35px;
    width: 800px;
    height: 1130px;
    font-family: "Montserrat", Arial, sans-serif;
  }
  .headline { font-style: italic; font-weight: 700; fill: #fff; font-size: 17px; }
  .headline-price { font-style: italic; font-weight: 800; fill: var(--orange); font-size: 32px; }
  .tagline { fill: var(--ink); font-size: 14px; font-weight: 500; }
  .tagline-strong { font-weight: 700; }
  .section-title { fill: var(--ink); font-size: 13.5px; font-weight: 700; }
  .service-label { fill: #fff; font-size: 10px; font-weight: 500; }
  .benefits-title { fill: var(--blue); font-size: 13px; font-weight: 700; }
  .benefit { fill: var(--ink); font-size: 12px; font-weight: 500; }
  .phone-number { fill: #fff; font-size: 31px; font-weight: 700; letter-spacing: 1px; }
  .brand-name { fill: var(--ink); font-size: 19px; font-weight: 700; }
  .footer-line { fill: var(--ink); font-size: 9.5px; font-weight: 500; }
</style>
</head>
<body>
<svg class="flyer" viewBox="0 0 538 760" xmlns="http://www.w3.org/2000/svg">
  <defs>
    <linearGradient id="room-tone" x1="0" y1="0" x2="0" y2="1">
      <stop offset="0" stop-color="#e6e4e2"/>
      <stop offset="0.45" stop-color="#eeedeb"/>
      <stop offset="1" stop-color="var(--paper)"/>
    </linearGradient>
    <linearGradient id="basin-tone" x1="0" y1="0" x2="1" y2="1">
      <stop offset="0" stop-color="var(--photo-light)"/>
      <stop offset="0.5" stop-color="var(--photo-mid)"/>
      <stop offset="1" stop-color="#f4f2ef"/>
    </linearGradient>
    <linearGradient id="tile-tone" x1="0" y1="0" x2="1" y2="1">
      <stop offset="0" stop-color="#e2b08a"/>
      <stop offset="1" stop-color="var(--photo-warm)"/>
    </linearGradient>
  </defs>

  <!-- background room -->
  <rect class="room-backdrop" x="0" y="0" width="538" height="760" fill="url(#room-tone)" role="img" aria-label="Heller, verblasster Badezimmerraum mit Waschtisch im Hintergrund"/>

  <!-- navy header field -->
  <polygon class="header-field" points="0,0 538,0 538,105 189,434 0,250" fill="var(--navy)"/>

  <!-- main image diamond -->
  <g class="hero-diamond" transform="translate(152 245) rotate(45)">
    <rect x="-106" y="-106" width="212" height="212" rx="30" fill="url(#basin-tone)" stroke="var(--blue)" stroke-width="11" role="img" aria-label="Modernes Badezimmer mit weißem Waschbecken, Mosaikfliesen und Tulpen"/>
  </g>

  <!-- orange accent diamond with detail image -->
  <g class="accent-diamond" transform="translate(327 231) rotate(45)">
    <rect x="-86" y="-86" width="172" height="172" rx="22" fill="var(--orange)"/>
  </g>
  <g class="detail-diamond" transform="translate(290 231) rotate(45)">
    <rect x="-67" y="-67" width="134" height="134" rx="14" fill="var(--navy)"/>
    <rect x="-61" y="-61" width="122" height="122" rx="11" fill="url(#tile-tone)" role="img" aria-label="Nahaufnahme einer Armatur vor warmen Mosaikfliesen"/>
  </g>

  <!-- headline -->
  <text class="headline" x="511" y="51" text-anchor="end">Ihr exklusives Bad zum</text>
  <text class="headline-price" x="511" y="95" text-anchor="end">Fixpreis!</text>

  <!-- tagline -->
  <text class="tagline" x="267" y="405">Wir montieren für Sie…</text>
  <text class="tagline" x="267" y="423">und das <tspan class="tagline-strong">„Alles aus einer Hand“</tspan>!</text>

  <!-- services -->
  <text class="section-title" x="27" y="470">Unsere Services</text>
  <g class="service-list">
    <rect x="27" y="481" width="227" height="159" fill="var(--panel)"/>
    <g stroke="#fff" stroke-width="1.2">
      <line x1="27" y1="520.5" x2="254" y2="520.5"/>
      <line x1="27" y1="560" x2="254" y2="560"/>
      <line x1="27" y1="600" x2="254" y2="600"/>
    </g>
    <g class="service-icons">
      <g transform="translate(35 491)"><polygon points="16,0 0,10 16,20" fill="var(--blue)"/><polygon points="16,10 8,15 16,20" fill="var(--orange)"/></g>
      <g transform="translate(35 531)"><polygon points="16,0 0,10 16,20" fill="var(--blue)"/><polygon points="16,10 8,15 16,20" fill="var(--orange)"/></g>
      <g transform="translate(35 570)"><polygon points="16,0 0,10 16,20" fill="var(--blue)"/><polygon points="16,10 8,15 16,20" fill="var(--orange)"/></g>
      <g transform="translate(35 610)"><polygon points="16,0 0,10 16,20" fill="var(--blue)"/><polygon points="16,10 8,15 16,20" fill="var(--orange)"/></g>
    </g>
    <text class="service-label" x="63" y="504">Markenbäder zum Online Preis</text>
    <text class="service-label" x="63" y="544">Wir montieren für Sie</text>
    <text class="service-label" x="63" y="583">Funktionalität und Ästhetik</text>
    <text class="service-label" x="63" y="617">Komplettlösungen mit rasche</text>
    <text class="service-label" x="63" y="629">Umsetzung</text>
  </g>

  <!-- benefits -->
  <text class="benefits-title" x="278" y="514">Ihre Vorteile</text>
  <text class="benefit" x="278" y="534">• Individuelle Badplanung</text>
  <text class="benefit" x="278" y="551">• Eigene Handwerker vor Ort</text>
  <text class="benefit" x="278" y="569">• Traumbad erlebniss</text>

  <!-- phone bar -->
  <rect class="phone-bar" x="0" y="664" width="409" height="50" fill="var(--blue)"/>
  <g class="phone-icon" transform="translate(24 656) rotate(-8)" fill="var(--navy)">
    <path d="M8 2 C4 4 0 10 2 22 C5 38 16 52 30 58 C36 60 40 58 43 54 L38 44 C36 42 33 42 31 44 L28 47 C20 42 14 34 12 25 L16 22 C18 20 18 17 17 15 Z"/>
  </g>
  <text class="phone-number" x="66" y="701">0800 314 926</text>

  <!-- brand -->
  <g class="brand">
    <rect x="400" y="630" width="130" height="88" fill="#fff"/>
    <rect x="416" y="664" width="14" height="14" fill="var(--blue)"/>
    <text class="brand-name" x="438" y="678">Badwerk</text>
  </g>

  <!-- footer -->
  <text class="footer-line" x="269" y="739" text-anchor="middle">Lindenweg 12, 2351 Wiesenau | www.badwerk-studio.at | office@badwerk-studio.at</text>
</svg>
</body>
</html>
```